Zielgruppe
Wir errichten neue Elektroanlagen für Einfamilenhäuser und Wohnungen.
Hallo,
wir möchten auf 12 Meter drei Banner spannen um die unschönen Rohre und Kabel zu verdecken. Jeder der drei Banner soll 400cm breit und 160cm hoch werden.
-Banner 1 links: Motivationsspruch groß, mittig - : Wer immer tut, was er schon kann, bleibt immer das, was er schon ist.
- Banner 2 mitte : Komfortzone ( Grafiken habe ich im Anhang von dem Aufbau der Komfortzone ) Toll wäre ein selbst erstelltes Design passend zum Unternehmen / Farben Schriftart etc.
-Banner 3 rechts: Motivationsspruch : Zusammenkommen ist ein Beginn, zusammenbleiben ist ein Fortschritt, zusammenarbeiten ist ein Erfolg.
- Design nach Vorgabe Druckblitz ( Datasheet) erstellen
Gundsätzlich wäre super, wenn alle 3 Designs/ Banner miteinander harmonieren. Alles andere ist der Kreativität überlassen.
Schriftart: Fira Sans / Montserrat
Wir würden uns über eine Zusammenarbeit freuen.
Beste Grüße

```html
<!DOCTYPE html>
<html lang="de">
<head>
<meta charset="utf-8">
<title>Banner Komfortzone</title>
<link href="https://fonts.googleapis.com/css2?family=Montserrat:wght@400;700&display=swap" rel="stylesheet">
<style>
  :root {
    --page-bg: #f3f3f4;
    --brand-blue: #1c9ad0;
    --zone-growth: #55a7d6;
    --zone-learn: #85b8df;
    --zone-fear: #d3e4f3;
    --zone-comfort: #ffffff;
    --text-light: #ffffff;
  }
  html, body {
    margin: 0;
    width: 1200px;
    height: 1200px;
    overflow: hidden;
    background: var(--page-bg);
  }
  .canvas {
    width: 1200px;
    height: 1200px;
    display: flex;
    align-items: center;
    justify-content: center;
  }
  .banner {
    width: 1100px;
    height: 439px;
    display: block;
    font-family: "Montserrat", sans-serif;
  }
  .zone-title { font-weight: 700; font-size: 24px; text-anchor: middle; letter-spacing: 0.3px; }
  .zone-word { font-weight: 400; font-size: 19px; text-anchor: middle; }
  .on-light { fill: var(--brand-blue); }
  .on-dark { fill: var(--text-light); }
</style>
</head>
<body>
<main class="canvas">
  <svg class="banner" viewBox="0 0 1753 700" role="img" aria-label="Stufenmodell von der Komfortzone zur Vision">
    <defs>
      <clipPath id="banner-area"><rect width="1753" height="700"/></clipPath>
      <linearGradient id="path-fade" x1="0" x2="1" y1="0" y2="0">
        <stop offset="0" stop-color="#1c9ad0"/>
        <stop offset="1" stop-color="#ffffff"/>
      </linearGradient>
      <linearGradient id="path-rise" x1="0" x2="1" y1="0" y2="0">
        <stop offset="0" stop-color="#ffffff"/>
        <stop offset="1" stop-color="#1c9ad0"/>
      </linearGradient>
    </defs>

    <g clip-path="url(#banner-area)">
      <rect class="banner-bg" width="1753" height="700" fill="var(--brand-blue)"/>
      <circle class="zone-growth" cx="796" cy="350" r="718" fill="var(--zone-growth)"/>
      <circle class="zone-learn" cx="601" cy="350" r="522" fill="var(--zone-learn)"/>
      <circle class="zone-fear" cx="415" cy="350" r="337" fill="var(--zone-fear)"/>
      <circle class="zone-comfort" cx="264" cy="350" r="187" fill="var(--zone-comfort)"/>
      <circle class="zone-vision" cx="1595" cy="350" r="81" fill="var(--zone-comfort)"/>

      <g class="progress-path">
        <rect x="264" y="347" width="187" height="5" fill="url(#path-fade)"/>
        <rect x="451" y="347" width="301" height="5" fill="url(#path-fade)"/>
        <rect x="752" y="347" width="371" height="5" fill="url(#path-fade)"/>
        <rect x="1123" y="347" width="392" height="5" fill="url(#path-fade)"/>
        <rect x="1515" y="347" width="80" height="5" fill="url(#path-rise)"/>
        <circle cx="264" cy="350" r="12" fill="var(--brand-blue)"/>
        <circle cx="1595" cy="350" r="11" fill="var(--brand-blue)"/>
      </g>

      <g class="idea-icon" fill="none" stroke="var(--text-light)" stroke-linecap="round">
        <path d="M1582 240 C1582 228 1572 224 1572 210 A23 23 0 1 1 1618 210 C1618 224 1608 228 1608 240 Z" stroke-width="3.5"/>
        <path d="M1598 196 L1589 214 L1598 214 L1592 230 L1604 208 L1595 208 L1600 196 Z" fill="var(--text-light)" stroke-width="1"/>
        <line x1="1586" y1="248" x2="1604" y2="248" stroke-width="4"/>
        <line x1="1586" y1="255" x2="1604" y2="255" stroke-width="4"/>
        <line x1="1590" y1="262" x2="1600" y2="262" stroke-width="4"/>
      </g>

      <g class="zone-titles">
        <text class="zone-title on-light" x="264" y="329">KOMFORTZONE</text>
        <text class="zone-title on-light" x="600" y="329">ANGSTZONE</text>
        <text class="zone-title on-dark" x="936" y="329">LERNZONE</text>
        <text class="zone-title on-dark" x="1318" y="329">WACHSTUMSZONE</text>
        <text class="zone-title on-light" x="1595" y="329">VISION</text>
      </g>

      <g class="zone-words">
        <text class="zone-word on-light" x="264" y="218">Sicherheit</text>
        <text class="zone-word on-light" x="338" y="270">Routine</text>
        <text class="zone-word on-light" x="336" y="400">Kontrolle</text>
        <text class="zone-word on-light" x="262" y="471">Gewohnheit</text>

        <text class="zone-word on-light" x="529" y="218">Unsicherheit</text>
        <text class="zone-word on-light" x="600" y="270">Ablehnung</text>
        <text class="zone-word on-light" x="600" y="400">Ausreden</text>
        <text class="zone-word on-light" x="529" y="471">Abbruch</text>

        <text class="zone-word on-dark" x="858" y="218">Neue Skills</text>
        <text class="zone-word on-dark" x="936" y="270">Erfahrungen</text>
        <text class="zone-word on-dark" x="936" y="400">Selbstvertrauen</text>
        <text class="zone-word on-dark" x="858" y="471">Zonenausbau</text>

        <text class="zone-word on-dark" x="1244" y="212">Zielerreichung</text>
        <text class="zone-word on-dark" x="1317" y="270">Sinnfindung</text>
        <text class="zone-word on-dark" x="1317" y="400">Selbstsicherheit</text>
        <text class="zone-word on-dark" x="1244" y="471">Zufriedenheit</text>
      </g>
    </g>
  </svg>
</main>
</body>
</html>
```